Redesign existing website.

I need a holidayhouse webdisain. Please review existing website: www.vaskemetsa.ee
I want to keep my logo.
Target Market(s)
Nature and sea enjoying holidaymakers, aged 30 to 70
Requirements
Must have
- 3 languages (English, Russian and Estonian)

```html
<!DOCTYPE html>
<html lang="et">
<head>
<meta charset="utf-8">
<title>Vaskemetsa Puhkemaja</title>
<link rel="stylesheet" href="https://fonts.googleapis.com/css2?family=Open+Sans:wght@400;600;700&family=Libre+Baskerville:ital@1&family=Fredoka:wght@600&display=swap">
<style>
:root{
  --blue:#0aa5ec;
  --blue-deep:#0a8fd4;
  --yellow:#fbe85a;
  --dark:#333333;
  --ink:#555555;
  --title:#8a8a8a;
  --white:#ffffff;
  --field:#1b8fcd;
}
*{box-sizing:border-box;margin:0;padding:0}
html,body{width:1200px;height:900px;overflow:hidden;background:var(--white)}
body{position:relative;font-family:"Open Sans",Arial,sans-serif;color:var(--ink)}
.abs{position:absolute}

/* hero */
.hero-photo{left:228px;top:0;width:745px;height:255px;
  background:linear-gradient(180deg,#b9cbd9 0%,#dfe7ee 30%,#9fb4c2 42%,#6f8fa3 55%,#5e8196 100%)}
.nav-tab{left:305px;top:0;width:563px;height:46px}
.brand-card{left:326px;top:0;width:150px;height:66px;background:var(--white);border-radius:0 0 6px 6px;
  box-shadow:0 1px 4px rgba(0,0,0,.25);transform:rotate(-2deg)}
.brand-mark{left:334px;top:6px;width:40px;height:50px;border-radius:4px;background:var(--blue)}
.brand-name{left:381px;top:17px;font-weight:700;font-size:12.5px;line-height:1;color:var(--blue);white-space:nowrap}
.main-nav{left:480px;top:11px;display:flex;gap:14px}
.main-nav a{color:var(--white);font-size:9.5px;line-height:1;font-weight:600;text-decoration:none}
.lang-label{left:820px;top:3px;font-size:7px;line-height:1;color:#222}
.flags{left:817px;top:13px;display:flex;gap:2px}
.flag{width:12px;height:9px;display:flex;flex-direction:column}
.flag i{flex:1}

.offer-badge{left:308px;top:95px;width:105px;height:55px}
.offer{left:308px;width:240px;height:38px}
.offer-thumb{left:0;top:0;width:48px;height:36px;border:2px solid var(--white);
  background:linear-gradient(180deg,#cfdbe4,#7d99ad)}
.offer-title{left:61px;top:-1px;font-size:10px;color:var(--white)}
.offer-text{left:61px;top:14px;width:115px;font-size:7px;line-height:12px;color:var(--white)}
.offer-more{left:179px;top:19px;width:58px;height:14px;background:var(--yellow);color:var(--blue-deep);
  font-size:7.5px;font-weight:600;text-align:center;line-height:14px}

/* cards */
.card{width:128px}
.card-photo{width:126px;height:81px;border:2px solid var(--blue)}
.card-title{margin:7px 0 0 3px;font-family:"Libre Baskerville",Georgia,serif;font-style:italic;font-weight:400;font-size:10px;line-height:13px;color:var(--title)}
.card-text{margin:3px 0 0 4px;font-size:7px;line-height:10.5px;color:var(--ink);width:124px}
.card-more{display:block;margin:8px 0 0 5px;width:59px;height:15px;background:var(--blue);color:var(--white);
  font-size:7.5px;font-weight:600;text-align:center;line-height:15px}

/* sidebar */
.side-box{left:757px;width:134px;background:var(--blue);border-radius:4px}
.side-ribbon{left:-7px;top:9px;width:138px;height:26px}
.side-list{list-style:none;position:absolute;left:18px;font-size:7px;color:var(--white)}
.side-list li{height:16.3px}

/* footer */
.foot-head{left:228px;top:687px;width:745px;height:35px;background:var(--dark)}
.foot-body{left:228px;top:722px;width:745px;height:151px;background:var(--blue)}
.foot-base{left:228px;top:873px;width:745px;height:27px;background:var(--dark);color:var(--white);
  font-size:7px;font-weight:600;text-align:center;line-height:27px}
.foot-title{top:698px;font-size:11px;font-weight:400;line-height:14px;color:var(--white)}
.about-text{left:309px;top:729px;width:169px;font-size:7px;font-weight:600;line-height:14.3px;color:var(--white);text-align:justify}
.contact-list{left:532px;top:730px;font-size:7px;font-weight:600;line-height:15.8px;color:var(--white)}
.social-title{left:532px;top:821px;font-size:11px;font-weight:600;color:var(--yellow)}
.social{top:840px;width:24px;height:24px;border-radius:50%;background:#6aa8c8;border:2px solid #cfe6f2}
.field{left:732px;width:113px;height:19px;background:var(--field);border:1px solid #6cc6f2;border-radius:2px;
  font-size:6.5px;color:#8fd0ef;padding:4px 5px}
.field-msg{width:166px;height:34px}
.submit{left:861px;top:853px;width:36px;height:13px;background:var(--yellow);color:var(--blue-deep);
  font-size:7px;font-weight:600;text-align:center;line-height:13px}
</style>
</head>
<body>

<header>
  <div class="abs hero-photo" role="img" aria-label="Calm sea bay with wooden stilt houses and a pier under a cloudy sky"></div>
  <svg class="abs nav-tab" viewBox="0 0 563 46" aria-hidden="true">
    <path d="M0 0H563V24Q563 30 556 30L6 45Q0 45 0 39Z" fill="var(--blue)"/>
  </svg>
  <div class="abs brand-card"></div>
  <div class="abs brand-mark"></div>
  <div class="abs brand-name">Vaskemetsa</div>
  <nav class="abs main-nav">
    <a href="#">Tutvustus</a><a href="#">Hinnakiri</a><a href="#">Asukoht</a><a href="#">Galerii</a><a href="#">Huvitavat</a><a href="#">Kontakt</a>
  </nav>
  <div class="abs lang-label">Language</div>
  <div class="abs flags">
    <span class="flag"><i style="background:#0072ce"></i><i style="background:#000"></i><i style="background:#fff"></i></span>
    <span class="flag"><i style="background:#fff"></i><i style="background:#0039a6"></i><i style="background:#d52b1e"></i></span>
    <span class="flag"><i style="background:#012169"></i><i style="background:#fff"></i><i style="background:#c8102e"></i></span>
  </div>

  <svg class="abs offer-badge" viewBox="0 0 105 55">
    <path d="M0 55V44A50 44 0 0 1 100 44V55Z" fill="var(--yellow)"/>
    <text x="10" y="28" font-family="Fredoka,sans-serif" font-weight="600" font-size="13" fill="var(--blue)">HOLIDAY</text>
    <text x="16" y="44" font-family="Fredoka,sans-serif" font-weight="600" font-size="11" fill="var(--blue)">MAKERS</text>
    <path d="M63 55A20 20 0 0 1 103 55Z" fill="var(--blue)" stroke="var(--white)" stroke-width="2"/>
    <text x="71" y="50" font-family="Fredoka,sans-serif" font-weight="600" font-size="10" fill="var(--white)">Offer</text>
  </svg>

  <div class="abs offer" style="top:163px">
    <div class="abs offer-thumb" role="img" aria-label="White seaside building"></div>
    <div class="abs offer-title">Lorem Ipsum</div>
    <div class="abs offer-text">But I must explain to you how all this mistaken idea of denouncing</div>
    <div class="abs offer-more">Read more</div>
  </div>
  <div class="abs offer" style="top:211px">
    <div class="abs offer-thumb" role="img" aria-label="White seaside building"></div>
    <div class="abs offer-title">Lorem Ipsum</div>
    <div class="abs offer-text">But I must explain to you how all this mistaken idea of denouncing</div>
    <div class="abs offer-more">Read more</div>
  </div>
</header>

<main>
  <article class="abs card" style="left:308px;top:281px">
    <div class="card-photo" role="img" aria-label="Rock arch in a blue sea" style="background:linear-gradient(180deg,#9cc6e8,#3c7fb2 55%,#2d5f86)"></div>
    <h3 class="card-title">Lorem Ipsum imple</h3>
    <p class="card-text">Lorem Ipsum is simply dummy text of the printing and typesetting ansd industry. Lorem Ipsum has been the industry's standard dummy text ever since the 1500s,</p>
    <a class="card-more">Read more</a>
  </article>
  <article class="abs card" style="left:459px;top:281px">
    <div class="card-photo" role="img" aria-label="Sunset over sea waves" style="background:linear-gradient(180deg,#3b5c86,#e9a24a 45%,#c66a2a 60%,#2b3e5a)"></div>
    <h3 class="card-title">Lorem Ipsum imple</h3>
    <p class="card-text">Lorem Ipsum is simply dummy text of the printing and typesetting ansd industry. Lorem Ipsum has been the industry's standard dummy text ever since the 1500s,</p>
    <a class="card-more">Read more</a>
  </article>
  <article class="abs card" style="left:611px;top:281px">
    <div class="card-photo" role="img" aria-label="Gazebo and palm trees by the shore" style="background:linear-gradient(90deg,#e5eef3,#4d7a56 45%,#3a8bbf)"></div>
    <h3 class="card-title">Lorem Ipsum imple</h3>
    <p class="card-text">Lorem Ipsum is simply dummy text of the printing and typesetting ansd industry. Lorem Ipsum has been the industry's standard dummy text ever since the 1500s,</p>
    <a class="card-more">Read more</a>
  </article>

  <article class="abs card" style="left:308px;top:477px">
    <div class="card-photo" role="img" aria-label="Terrace with pool overlooking the sea" style="background:linear-gradient(90deg,#2d7fc6,#6bb0e0 55%,#e8e4da)"></div>
    <h3 class="card-title" style="margin-top:11px">Lorem Ipsum imple</h3>
    <p class="card-text">Lorem Ipsum is simply dummy text of the printing and typesetting ansd industry. Lorem Ipsum has been the industry's standard dummy text ever since the 1500s,</p>
    <a class="card-more">Read more</a>
  </article>
  <article class="abs card" style="left:459px;top:477px">
    <div class="card-photo" role="img" aria-label="Bay with stilt houses under a cloudy sky" style="background:linear-gradient(180deg,#b8d0e4,#eaf0f4 35%,#4f7fa3 60%,#2f5b7e)"></div>
    <h3 class="card-title" style="margin-top:11px">Lorem Ipsum imple</h3>
    <p class="card-text">Lorem Ipsum is simply dummy text of the printing and typesetting ansd industry. Lorem Ipsum has been the industry's standard dummy text ever since the 1500s,</p>
    <a class="card-more">Read more</a>
  </article>
  <article class="abs card" style="left:611px;top:477px">
    <div class="card-photo" role="img" aria-label="Rocky shore in calm blue water" style="background:linear-gradient(160deg,#3a7fb6,#2a6ea3 55%,#8a7a62)"></div>
    <h3 class="card-title" style="margin-top:11px">Lorem Ipsum imple</h3>
    <p class="card-text">Lorem Ipsum is simply dummy text of the printing and typesetting ansd industry. Lorem Ipsum has been the industry's standard dummy text ever since the 1500s,</p>
    <a class="card-more">Read more</a>
  </article>

  <aside class="abs side-box" style="top:275px;height:184px">
    <svg class="abs side-ribbon" viewBox="0 0 138 26">
      <path d="M0 8Q0 2 6 2H134Q138 2 138 9V13Q138 19 132 19H10Q3 19 1 26Z" fill="var(--yellow)"/>
      <path d="M1 26Q0 19 8 19H12Z" fill="#6d5a1a"/>
      <text x="14" y="14" font-family="Open Sans,sans-serif" font-weight="600" font-size="7.5" fill="var(--blue-deep)">DESTINATIONS</text>
    </svg>
    <ul class="side-list" style="top:35px">
      <li>Lorem Ipsum</li><li>Simply dummy</li><li>Text of the printing</li><li>Typesetting industry</li><li>Lorem Ipsum</li><li>industry's standard</li><li>Dummy text</li><li>Ever since the</li>
    </ul>
  </aside>
  <aside class="abs side-box" style="top:470px;height:184px">
    <svg class="abs side-ribbon" viewBox="0 0 138 26">
      <path d="M0 8Q0 2 6 2H134Q138 2 138 9V13Q138 19 132 19H10Q3 19 1 26Z" fill="var(--yellow)"/>
      <path d="M1 26Q0 19 8 19H12Z" fill="#6d5a1a"/>
      <text x="14" y="14" font-family="Open Sans,sans-serif" font-weight="600" font-size="7.5" fill="var(--blue-deep)">DESTINATIONS</text>
    </svg>
    <ul class="side-list" style="top:38px">
      <li>Lorem Ipsum</li><li>Simply dummy</li><li>Text of the printing</li><li>Typesetting industry</li><li>Lorem Ipsum</li><li>industry's standard</li><li>Dummy text</li><li>Ever since the</li>
    </ul>
  </aside>
</main>

<footer>
  <div class="abs foot-head"></div>
  <div class="abs foot-body"></div>
  <h4 class="abs foot-title" style="left:309px">About US</h4>
  <h4 class="abs foot-title" style="left:532px">Contact us</h4>
  <h4 class="abs foot-title" style="left:732px">Contact form</h4>

  <p class="abs about-text">Majutus 5-le puhkajale. Teid ootab mugav 2 magamistoaga puhkemaja. Asume põhjaranni&shy;kul, Kadaka poolsaarel, Vaske külas, Rannavalla looduspargis. Linnast vaid 58 km kaugusel. Vaske on sobiv koht mõnusaks, rahulikuks puh&shy;kuseks. Sillerdavat merd ja kauneid päikesel&shy;oojanguid võib nautida lausa maja aknast.</p>

  <div class="abs contact-list">
    Metsa talu, Vaske küla, Rannavalla vald,<br>
    Harjumaa 74999<br>
    Phone : +372 55 01 234<br>
    Email :&nbsp; info@vaskemetsa.ee<br>
    Fax &nbsp;&nbsp;: &nbsp;1200345, 5500678, 55901
  </div>
  <div class="abs social-title">Social media</div>
  <span class="abs social" style="left:532px"></span>
  <span class="abs social" style="left:560px"></span>
  <span class="abs social" style="left:588px"></span>

  <div class="abs field" style="top:733px">Name</div>
  <div class="abs field" style="top:759px">email address</div>
  <div class="abs field" style="top:785px">phone</div>
  <div class="abs field field-msg" style="top:811px">Message</div>
  <div class="abs submit">Submit</div>

  <div class="abs foot-base">Designed and Developed By VASKEMETSA PUHKEMAJA</div>
</footer>

</body>
</html>
```